Design a newsletter for a crypto gateway payment company

The project is about making the design for a newsletter (sent by email) for a crypto payment gateway. The design should include all usual and necessary parts found in a newsletter (header, one main article with illustration and link to the full content, some secondary articles with or without illustration and link to the company blog, footer with links to unsubscribe page and various information about the company, section separator, secondary articles ...).
The design may re-use some elements from the company web site https://quorvelpay.io, but feel free to innovate.
The design should be responsive and be as good in all email clients and all sizes of display from handset to desktop with everything in between.
I've added a few screenshot of the previous newsletter as they were sent to users.
Good luck and be an artist. No AI stuff, please.

```html
<!DOCTYPE html>
<html lang="en">
<head>
<meta charset="utf-8">
<title>QuorvelPay Newsletter</title>
<link href="https://fonts.googleapis.com/css2?family=Outfit:wght@300;400;700&display=swap" rel="stylesheet">
<style>
  :root {
    --ink: #0d0f2b;
    --ink-soft: #1c1f3a;
    --page: #fafafa;
    --hero: #fbfbfc;
    --white: #ffffff;
    --rule: #e4e4e8;
    --glow-deep: #021026;
    --glow-mid: #0a4d8c;
    --glow-bright: #1fc8f2;
  }
  * { box-sizing: border-box; margin: 0; padding: 0; }
  html, body { width: 1102px; height: 1200px; overflow: hidden; }
  body {
    position: relative;
    background: var(--page);
    color: var(--ink);
    font-family: "Outfit", sans-serif;
    font-weight: 300;
  }
  a { color: inherit; }
  .brand {
    position: absolute; top: 22px; left: 0; width: 100%;
    text-align: center; font-weight: 700; font-size: 32px; letter-spacing: -1px;
    color: #111;
  }
  .hero-band {
    position: absolute; top: 108px; left: 0; width: 100%; height: 328px;
    background: var(--hero);
  }
  .hero-title {
    position: absolute; left: 141px; top: 144px;
    font-size: 36px; line-height: 39px; font-weight: 300; letter-spacing: 0.2px;
  }
  .hero-text {
    position: absolute; left: 141px; top: 239px; width: 370px;
    font-size: 11.3px; line-height: 18.4px;
  }
  .read-more { font-size: 11.5px; font-weight: 400; color: #333; }
  .hero-link { position: absolute; left: 141px; top: 362px; }
  .hero-visual {
    position: absolute; left: 576px; top: 120px; width: 385px; height: 284px;
    border-radius: 3px;
    background: radial-gradient(circle at 76% 50%, var(--glow-bright) 0%, var(--glow-mid) 28%, var(--glow-deep) 62%);
  }
  .hero-caption {
    position: absolute; left: 547px; top: 379px; width: 155px; height: 54px;
    background: var(--white); border-radius: 4px;
    box-shadow: 0 6px 14px rgba(0,0,0,0.07);
    display: flex; align-items: center; justify-content: center;
    font-size: 11.3px; font-weight: 400;
  }
  .section-title {
    position: absolute; top: 535px; left: 0; width: 100%; text-align: center;
    font-size: 37px; font-weight: 300;
  }
  .title-dash { position: absolute; height: 2px; background: var(--ink); }
  .section-dash { left: 532px; top: 595px; width: 27px; }
  .section-intro {
    position: absolute; top: 618px; left: 356px; width: 378px; text-align: center;
    font-size: 11.3px; line-height: 18.4px;
  }
  .feature { position: absolute; top: 716px; width: 300px; }
  .feature-left { left: 182px; }
  .feature-right { left: 626px; }
  .feature h3 { font-size: 19px; line-height: 23px; font-weight: 300; }
  .feature .title-dash { position: static; width: 17px; height: 1.5px; margin: 19px 0 0 2px; }
  .feature p { margin: 22px 0 0 1px; font-size: 11.3px; line-height: 18.4px; }
  .feature .read-more { display: inline-block; margin-top: 12px; font-size: 10px; color: var(--ink); }
  .feature-divider {
    position: absolute; left: 552px; top: 718px; width: 1px; height: 242px;
    background: var(--rule);
  }
  .cta {
    position: absolute; top: 1075px; left: 0; width: 100%; text-align: center;
    font-size: 15.5px; font-weight: 400;
  }
  .cta-icon { position: absolute; left: 539px; top: 1114px; }
  .footer-rule { position: absolute; left: 68px; top: 1163px; width: 952px; height: 1px; background: #d6d6da; }
  .footer {
    position: absolute; left: 68px; top: 1174px; width: 952px;
    display: flex; justify-content: space-between; align-items: center;
    font-size: 11px; font-weight: 400;
  }
  .unsubscribe { display: flex; align-items: center; gap: 6px; text-decoration: none; font-size: 11.5px; }
</style>
</head>
<body>
  <header class="brand">QuorvelPay</header>

  <section>
    <div class="hero-band"></div>
    <h1 class="hero-title">Relive the joy of<br>reading Newsletters</h1>
    <p class="hero-text">Ac pulvinar nibh quam purus malesuada. Purus est tristique vel netus dictum nulla. Metus mi placerat euismod nascetur malesuada odio. Sed nec id arcu commodo scelerisque metus sapien nullam. Est curabitur nunc non nec convallis ornare enim aenean. Dictum habitasse amet proin urna venenatis elit ut pulvinar. Morbi mattis at egestas ac nibh eget ut.</p>
    <a class="read-more hero-link" href="https://quorvelpay.io">Read More</a>
    <div class="hero-visual" role="img" aria-label="Glowing blue digital coin on a circuit board background"></div>
    <div class="hero-caption">Dictum habitasse amet</div>
  </section>

  <section>
    <h2 class="section-title">How It works</h2>
    <div class="title-dash section-dash"></div>
    <p class="section-intro">Purus est tristique vel netus dictum nulla. Metus mi placerat euismod nascetur malesuada odio.</p>

    <article class="feature feature-left">
      <h3>Purus est tristique vel netus dictum nulla nunc</h3>
      <div class="title-dash"></div>
      <p>Ac pulvinar nibh quam purus malesuada. Purus est tristique vel netus dictum nulla. Metus mi placerat euismod nascetur malesuada odio. Sed nec id arcu commodo scelerisque metus sapien nullam. Est curabitur nunc non nec convallis ornare enim aenean. Dictum habitasse amet proin urna venenatis elit ut pulvinar. Morbi mattis at egestas ac nibh eget ut.</p>
      <a class="read-more" href="https://quorvelpay.io">Read More</a>
    </article>
    <div class="feature-divider"></div>
    <article class="feature feature-right">
      <h3>Purus est tristique vel netus dictum nulla nunc</h3>
      <div class="title-dash"></div>
      <p>Ac pulvinar nibh quam purus malesuada. Purus est tristique vel netus dictum nulla. Metus mi placerat euismod nascetur malesuada odio. Sed nec id arcu commodo scelerisque metus sapien nullam. Est curabitur nunc non nec convallis ornare enim aenean. Dictum habitasse amet proin urna venenatis elit ut pulvinar. Morbi mattis at egestas ac nibh eget ut.</p>
      <a class="read-more" href="https://quorvelpay.io">Read More</a>
    </article>
  </section>

  <section>
    <a class="cta" href="https://quorvelpay.io">Start Enjoying The Benefits Of Digital Currencies Payments &amp; Payouts</a>
    <svg class="cta-icon" width="24" height="24" viewBox="0 0 24 24" aria-hidden="true">
      <circle cx="12" cy="12" r="11" fill="none" stroke="#0d0f2b" stroke-width="1.4"/>
      <path d="M7 12h9M12.5 8.2 16.3 12l-3.8 3.8" fill="none" stroke="#0d0f2b" stroke-width="1.6" stroke-linecap="round" stroke-linejoin="round"/>
    </svg>
  </section>

  <div class="footer-rule"></div>
  <footer class="footer">
    <span>© Quorvel Technologies Pte. Ltd. 2024 | All Rights Reserved</span>
    <a class="unsubscribe" href="https://quorvelpay.io">Unsubscribe
      <svg width="10" height="10" viewBox="0 0 10 10" aria-hidden="true"><path d="M1 5h7.5M5.5 1.8 8.7 5 5.5 8.2" fill="none" stroke="#0d0f2b" stroke-width="1.3" stroke-linecap="round" stroke-linejoin="round"/></svg>
    </a>
  </footer>
</body>
</html>
```